Album Cover Art for New Single

Independent singer-songwriter and pianist, seeking design work for a new single "Walk Along the Harbor". Christian & Gospel music format. See attached for master recording.

This single is personal for me, so I'm looking for an image that really captures the heart of the message. Redemption, forgiveness, prodigals returning home to a loving father.
Updates

Target Market(s)

Millenials

Colors

Designer to choose colors to be used in the design.

Requirements
Must have
• simple graphic, must include the following text:
• Walk Along the Harbor
• Dale Fennimore
Should not have
• Avoid "cheesy" look and feel.

```html
<!DOCTYPE html>
<html lang="en">
<head>
<meta charset="utf-8">
<title>Walk Along the Harbor — Dale Fennimore</title>
<link rel="stylesheet" href="https://fonts.googleapis.com/css2?family=Cormorant+Garamond:wght@500&family=Fira+Sans+Extra+Condensed:wght@300&display=swap">
<style>
  :root {
    --tree-shadow: #2b3529;
    --tree-mid: #4a5744;
    --sky-haze: #b9c4c6;
    --road-grey: #8b8d8c;
    --road-dark: #6f7271;
    --type-white: #ffffff;
  }
  html, body {
    margin: 0;
    padding: 0;
    width: 1200px;
    height: 1200px;
    overflow: hidden;
    background: #ffffff;
  }
  .cover {
    position: relative;
    width: 1200px;
    height: 1200px;
    overflow: hidden;
  }
  .cover-scene {
    position: absolute;
    inset: 0;
    background:
      radial-gradient(ellipse 260px 340px at 50% 10%, var(--sky-haze) 0%, rgba(185,196,198,0) 100%),
      linear-gradient(180deg, var(--tree-shadow) 0%, var(--tree-mid) 32%, var(--road-dark) 52%, var(--road-grey) 75%, var(--road-dark) 100%);
  }
  .artist-name {
    position: absolute;
    top: 50px;
    left: 0;
    width: 100%;
    margin: 0;
    text-align: center;
    font-family: "Cormorant Garamond", Georgia, serif;
    font-weight: 500;
    font-size: 28px;
    letter-spacing: 0.42em;
    text-transform: uppercase;
    color: var(--type-white);
  }
  .single-title {
    position: absolute;
    inset: 0;
    width: 1200px;
    height: 1200px;
  }
  .single-title text {
    font-family: "Fira Sans Extra Condensed", "Arial Narrow", sans-serif;
    font-weight: 300;
    font-size: 320px;
    fill: var(--type-white);
  }
</style>
</head>
<body>
  <main class="cover">
    <div class="cover-scene" role="img" aria-label="Photograph of a woman with long red hair seen from behind, arms raised, standing in the middle of a tree-lined country road"></div>
    <p class="artist-name">Dale Fennimore</p>
    <svg class="single-title" viewBox="0 0 1200 1200" role="heading" aria-level="1" aria-label="Walk Along the Harbor">
      <text x="75" y="700" textLength="1000" lengthAdjust="spacingAndGlyphs" transform="rotate(-12 75 700)">WALK ALONG</text>
      <text x="110" y="985" textLength="1030" lengthAdjust="spacingAndGlyphs" transform="rotate(-12 110 985)">THE HARBOR</text>
    </svg>
  </main>
</body>
</html>
```